Power resources consultancy needs a business card design

Business card should represent civil engineering infrastructure projects such as roads, bridges, tunnels, rail, rail, pipelines, structures and resource infrastructure

Industry/Entity Type

Business

```html
<!DOCTYPE html>
<html lang="en">
<head>
<meta charset="utf-8">
<title>KVT — Business Card</title>
<link rel="stylesheet" href="https://fonts.googleapis.com/css2?family=Fira+Sans+Condensed:wght@600&display=swap">
<style>
  :root {
    --card-navy: #000f78;
    --accent-gold: #d7901f;
    --text-white: #ffffff;
  }
  html, body {
    margin: 0;
    padding: 0;
    width: 1200px;
    height: 676px;
    overflow: hidden;
    background: var(--card-navy);
  }
  .card {
    position: relative;
    width: 1200px;
    height: 676px;
    background: var(--card-navy);
    font-family: "Fira Sans Condensed", "Arial Narrow", sans-serif;
    font-weight: 600;
    color: var(--text-white);
  }
  .brand {
    position: absolute;
    left: 184px;
    top: 150px;
    width: 300px;
    display: flex;
    flex-direction: column;
    align-items: center;
  }
  .brand-mark {
    display: block;
  }
  .brand-name {
    margin-top: 168px;
    font-size: 92px;
    line-height: 1;
    letter-spacing: 2px;
    color: var(--text-white);
  }
  .divider {
    position: absolute;
    left: 591px;
    top: 129px;
    width: 4px;
    height: 434px;
    background: var(--accent-gold);
  }
  .services {
    position: absolute;
    left: 634px;
    top: 118px;
    margin: 0;
    padding: 0;
    list-style: none;
  }
  .services li {
    font-size: 45px;
    line-height: 67.4px;
    color: var(--text-white);
  }
</style>
</head>
<body>
  <main class="card">
    <div class="brand">
      <svg class="brand-mark" width="90" height="90" viewBox="0 0 90 90" aria-hidden="true">
        <circle cx="45" cy="45" r="40" fill="var(--accent-gold)"/>
      </svg>
      <div class="brand-name">KVT</div>
    </div>

    <div class="divider"></div>

    <ul class="services">
      <li>roads</li>
      <li>bridges</li>
      <li>tunnels</li>
      <li>rail</li>
      <li>pipelines</li>
      <li>structures</li>
      <li>resource infrastructure</li>
    </ul>
  </main>
</body>
</html>
```